Artificial Intelligence based service LanePilot.ai

Looking for a website for service designed for driving schools to deliver AI based solutions and features. File are to include various pages from contact to list of services to faqs, demos and more. we are looking for a website for AI based service for driving schools. services will include things like chat bots, voice agent, document processing and ai based marketing.

Target Market(s)

driving school owners and managers.

Industry/Entity Type

software and AI

Number of Pages Required

4 page

Font styles to use
Sans Serif

Requirements
Must have
• clean and easy to navigate pages. responsive. also delivery via FIGMA.

```html
<!DOCTYPE html>
<html lang="en">
<head>
<meta charset="utf-8">
<title>LanePilot.ai – AI Voice Agents for Driving Schools</title>
<link href="https://fonts.googleapis.com/css2?family=Exo+2:wght@400;500;600;700&family=Poppins:wght@300;400;500;600&display=swap" rel="stylesheet">
<style>
:root{
  --navy:#0f2350;
  --navy-deep:#0b1d45;
  --green:#6cb36a;
  --green-dark:#3f8a3f;
  --green-soft:#e3f1df;
  --text:#2b3550;
  --muted:#5b6478;
  --card:#f3f6f9;
  --line:#dfe6ea;
  --blue-panel:#a9cadb;
  --white:#ffffff;
}
*{box-sizing:border-box;margin:0;padding:0}
html,body{width:1200px;height:4364px;overflow:hidden}
body{position:relative;font-family:'Poppins',sans-serif;color:var(--text);background:var(--white)}
.abs{position:absolute}
h1,h2,h3,.display{font-family:'Exo 2',sans-serif;font-weight:500}
.accent{color:var(--green);font-weight:600}
.photo{position:absolute;overflow:hidden}

/* header */
.hero-bg{left:0;top:0;width:1200px;height:627px;background:linear-gradient(180deg,#fff 0%,#fff 45%,#e0efd9 100%)}
.brand{left:112px;top:18px;font-family:'Poppins',sans-serif;font-weight:600;font-size:24px;color:var(--navy);display:flex;align-items:center;gap:10px;white-space:nowrap}
.brand .dot{width:16px;height:16px;background:var(--green);border-radius:50%}
.nav{left:366px;top:38px;display:flex;gap:26px;font-size:13px;color:var(--navy);white-space:nowrap}
.btn{position:absolute;display:flex;align-items:center;justify-content:center;font-size:13px;border-radius:3px;white-space:nowrap}
.btn-outline{border:1.5px solid var(--navy);color:var(--navy);background:#fff}
.btn-green{background:var(--green);color:#fff}

/* hero */
.hero-small{left:112px;top:172px;font-size:30px;color:var(--navy);font-family:'Exo 2',sans-serif}
.hero-title{left:110px;top:208px;font-size:50px;line-height:55px;color:var(--navy);font-weight:700;white-space:nowrap}
.hero-title .accent{font-weight:700}
.hero-photo{left:570px;top:132px;width:464px;height:356px;border:5px solid var(--green);border-top-right-radius:90px;background:linear-gradient(135deg,#c7d3de,#8fa3b5 50%,#5f7183)}
.tag{position:absolute;background:#fff;border-radius:24px;box-shadow:0 4px 14px rgba(15,35,80,.12);display:flex;align-items:center;gap:10px;font-size:12px;color:var(--navy);padding:6px 14px 6px 6px;white-space:nowrap}
.tag i{width:30px;height:30px;border-radius:50%;background:#eef2f5;border:2px solid var(--navy);display:block}
.badge247{left:960px;top:385px;width:105px;height:105px;border-radius:50%;background:var(--navy);border:6px solid var(--green);color:#fff;display:flex;align-items:center;justify-content:center;font-weight:600;font-size:18px}

/* feature strip */
.feature{position:absolute;top:556px;width:314px;height:112px;background:var(--card);border-radius:8px;display:flex;align-items:center;gap:22px;padding-left:36px;font-size:16px;color:var(--navy);box-shadow:0 2px 8px rgba(0,0,0,.04)}
.feature .ic{width:58px;height:58px;border-radius:50%;background:#fff;display:flex;align-items:center;justify-content:center;flex:none}
.ghost{position:absolute;font-family:'Exo 2',sans-serif;font-size:118px;color:transparent;-webkit-text-stroke:1px #e4e8ed;letter-spacing:3px;white-space:nowrap;font-weight:500}

/* why */
.why-photo{left:200px;top:803px;width:353px;height:385px;border-radius:176px 176px 0 0;border:3px solid var(--green);border-bottom:none;background:linear-gradient(180deg,#9cc4e2,#c9dcec 55%,#3b4047)}
.check-card{left:110px;top:935px;width:186px;height:112px;background:#fff;border-radius:6px;box-shadow:0 4px 14px rgba(0,0,0,.12);padding:14px 10px;font-size:10px;color:var(--navy)}
.check-card li{list-style:none;display:flex;align-items:center;gap:6px;margin-bottom:8px;white-space:nowrap}
.tick{width:11px;height:11px;border-radius:50%;background:var(--green);display:inline-block;flex:none}
.why-bar{left:192px;top:1190px;width:839px;height:18px;background:var(--green)}
.why-sq{left:1039px;top:1190px;width:34px;height:18px;background:var(--green)}
.why-title{left:688px;top:888px;font-size:36px;line-height:44px;color:var(--navy);white-space:nowrap}
.why-copy{left:688px;top:985px;width:360px;font-size:11.5px;line-height:20px;color:var(--text)}

/* services */
.sec-title{position:absolute;left:0;width:1200px;text-align:center;font-size:36px;color:var(--navy)}
.service{position:absolute;top:1325px;width:232px;height:243px;background:linear-gradient(180deg,#eef4f7,#fff);border-radius:6px;text-align:center}
.service h3{font-family:'Poppins',sans-serif;font-weight:400;font-size:16px;color:var(--navy);margin-top:24px}
.service .view{display:inline-block;margin-top:14px;border:1.5px solid var(--green);color:var(--green);font-size:11px;padding:5px 16px;border-radius:2px}
.service .photo{left:16px;top:107px;width:200px;height:136px;border-radius:4px 4px 0 0}

/* problems */
.problems-bg{left:0;top:1627px;width:1200px;height:560px;background:linear-gradient(180deg,#f1f3f6,#e9edf1)}
.kp{left:0;width:1200px;top:1678px;text-align:center;font-size:13px;color:var(--navy)}
.pill{position:absolute;width:260px;height:65px;background:#fff;border-radius:8px;display:flex;align-items:center;gap:14px;font-size:16px;color:var(--navy);padding:0 14px;white-space:nowrap}
.pill.right{justify-content:flex-end}
.pill .circ{width:40px;height:40px;border-radius:50%;background:var(--navy);border:4px solid #dfe5ee;flex:none}
.phone{left:559px;top:1766px;width:141px;height:288px;border:6px solid #2a2f38;border-radius:20px;background:linear-gradient(180deg,#2fa179,#6bbf6d);color:#fff;text-align:center;overflow:hidden}
.phone .plogo{font-weight:600;font-size:14px;margin-top:58px}
.phone p{font-size:14px;line-height:17px;margin-top:16px;font-style:italic;font-weight:500}
.phone .foot{position:absolute;bottom:0;left:0;width:100%;height:24px;background:#fff}
.robot{left:455px;top:1880px;width:130px;height:160px;border-radius:60px 60px 40px 40px;background:linear-gradient(180deg,#e7eef4,#b9c8d5)}
.result{left:0;width:1200px;top:2098px;text-align:center;font-size:13px;color:var(--navy)}
.result b{color:var(--green);font-weight:400}

/* benefit cards */
.bcard{position:absolute;width:481px;height:141px;background:linear-gradient(90deg,#eef3f7,#e8f3e6);border-radius:6px}
.bcard .ic{position:absolute;left:30px;top:32px;width:76px;height:76px;border-radius:50%;background:#dde8ee;display:flex;align-items:center;justify-content:center}
.bcard h3{position:absolute;left:157px;top:28px;font-family:'Poppins',sans-serif;font-weight:400;font-size:16px;color:var(--navy);white-space:nowrap}
.bcard p{position:absolute;left:157px;top:54px;width:300px;font-size:11px;line-height:17px;color:var(--muted)}
.bcard p.res{top:92px;color:var(--green)}
.bcard p.res b{font-weight:600}
.bcard.framed{background:#fff;border:5px solid var(--green);width:520px;height:153px}
.side-bar{height:20px;background:var(--green)}

/* real benefits */
.rb-panel{left:122px;top:2827px;width:956px;height:407px;background:var(--blue-panel);border-radius:8px}
.rb-title{left:166px;top:2884px;font-size:35px;line-height:40px;color:#fff}
.rb-title b{font-weight:700}
.rb-list{left:170px;top:2978px;list-style:none;color:#fff;font-size:15px}
.rb-list li{display:flex;align-items:center;gap:12px;height:33.5px;white-space:nowrap}
.rb-list .tick{background:#fff;width:14px;height:14px}
.rb-photo{left:615px;top:2848px;width:444px;height:367px;border-radius:6px;background:linear-gradient(135deg,#1f2630,#4b5663 50%,#2a3038)}

/* cta */
.cta{left:0;top:3275px;width:1200px;height:310px;background:linear-gradient(100deg,#2f7d3a 0%,#5ea85b 55%,#b6e6a5 100%)}
.cta h2{position:absolute;left:0;width:1200px;top:50px;text-align:center;color:#fff;font-size:56px;line-height:62px}
.cta h2 b{font-weight:700}
.cta p{position:absolute;left:0;width:1200px;top:186px;text-align:center;color:#fff;font-size:15px}
.cta .btn{top:218px;height:43px;font-weight:500}
.btn-ghost{border:1.5px solid rgba(255,255,255,.85);color:#fff}
.btn-white{background:#fff;color:var(--navy)}

/* testimonial */
.quote-card{left:332px;top:3682px;width:534px;height:234px;background:linear-gradient(180deg,#e9f0f5,#dbe7ef);border-radius:30px}
.quote-mark{left:354px;top:3700px;font-family:'Exo 2',sans-serif;font-size:90px;line-height:90px;color:#c3d2de}
.avatar{left:574px;top:3703px;width:50px;height:50px;border-radius:50%;background:#c9d3dd;border:3px solid #a8d39c}
.q-name{left:332px;width:534px;top:3771px;text-align:center;font-size:13px;color:var(--navy)}
.q-name b{color:#2f4fa8;font-weight:500}
.q-text{left:410px;width:378px;top:3793px;text-align:center;font-size:11px;line-height:18px;color:var(--text)}
.stars{left:332px;width:534px;top:3866px;text-align:center;color:#f3b321;font-size:16px;letter-spacing:2px}
.arrow{width:18px;height:18px;border-radius:50%;border:1.5px solid #9aa5b3}

/* footer */
.footer{left:0;top:4071px;width:1200px;height:293px;background:var(--navy-deep);color:#fff}
.f-desc{left:112px;top:4204px;width:240px;font-size:10px;line-height:17px;color:#d9deea}
.f-div{top:4110px;width:1px;height:175px;background:#34466f}
.f-head{font-size:14px;font-weight:500;white-space:nowrap}
.f-links{list-style:none;font-size:9.5px;line-height:20.5px;color:#d9deea;white-space:nowrap}
.f-social{display:flex;align-items:center;gap:12px;font-size:10px;color:#d9deea;height:36px;white-space:nowrap}
.f-social i{width:22px;height:22px;border-radius:50%;border:1.5px solid #fff;display:block}
.f-input{left:864px;top:4146px;width:223px;height:37px;border:1px solid #8b98b8;font-size:10px;color:#d9deea;padding:12px 16px}
.f-copy{left:0;width:1200px;top:4335px;text-align:center;font-size:9px;color:#d9deea}
</style>
</head>
<body>

<!-- Header & hero -->
<div class="abs hero-bg"></div>
<div class="abs brand"><span class="dot"></span>LanePilot.ai</div>
<nav class="abs nav"><span>Services</span><span>Why Driving Schools</span><span>About</span><span>Pricing</span><span>FAQS</span><span>Demos</span></nav>
<div class="btn btn-outline" style="left:886px;top:30px;width:86px;height:36px">Login</div>
<div class="btn btn-green" style="left:979px;top:30px;width:108px;height:36px">Contact Us</div>

<div class="abs hero-small">Boost Your</div>
<h1 class="abs hero-title">Driving School<br>With a <span class="accent">24/7</span><br>Voice Agent</h1>
<div class="btn btn-green" style="left:112px;top:398px;width:221px;height:41px;font-weight:500;font-size:12px">Need Help Getting Started?</div>

<div class="photo hero-photo" role="img" aria-label="Humanoid robot standing beside a smiling young driver at the wheel of a car"></div>
<div class="tag" style="left:766px;top:118px"><i></i>Document Processing</div>
<div class="tag" style="left:932px;top:194px"><i></i>Chat Bots</div>
<div class="tag" style="left:508px;top:362px"><i></i>Voice Agent</div>
<div class="tag" style="left:510px;top:422px"><i></i>AI Based Marketing</div>
<div class="abs badge247">24/7</div>

<div class="feature" style="left:112px"><span class="ic"><svg width="34" height="30" viewBox="0 0 34 30" fill="none" stroke="#0f2350" stroke-width="2"><rect x="2" y="3" width="30" height="24" rx="3"/><path d="M8 3v24M13 10h3M19 10h3M25 10h3M13 16h3M19 16h3M25 16h3M13 22h3M19 22h3M25 22h3"/></svg></span>Automate Calls.</div>
<div class="feature" style="left:442px"><span class="ic"><svg width="36" height="30" viewBox="0 0 36 30" fill="none" stroke="#0f2350" stroke-width="2"><path d="M2 11 18 3l16 8-16 8z"/><path d="M8 14v8c6 5 14 5 20 0v-8"/></svg></span>Never Miss a<br>Student Again.</div>
<div class="feature" style="left:773px"><span class="ic"><svg width="34" height="30" viewBox="0 0 34 30" fill="none" stroke="#0f2350" stroke-width="2"><rect x="2" y="2" width="22" height="17" rx="3"/><path d="M8 19v6l6-6M24 10h6a2 2 0 0 1 2 2v10h-4v5l-5-5h-6"/><path d="M11 8a2 2 0 1 1 3 2v2M13 15v.5"/></svg></span>Answer Questions<br>Instantly.</div>

<div class="ghost" style="left:112px;top:670px">LanePilot.ai</div>

<!-- Why section -->
<div class="photo why-photo" role="img" aria-label="Cheerful older woman at a steering wheel holding a phone to her ear"></div>
<ul class="abs check-card">
  <li><span class="tick"></span>Juggling Lesson Schedules</li>
  <li><span class="tick"></span>Constant Phone Calls</li>
  <li><span class="tick"></span>student questions</li>
  <li><span class="tick"></span>Staff changes</li>
</ul>
<div class="tag" style="left:416px;top:1118px"><i></i>Answers the Phone</div>
<div class="abs why-bar"></div>
<div class="abs why-sq"></div>
<h2 class="abs why-title">Why Driving Schools<br>Choose <span class="accent">Voice Agents</span></h2>
<p class="abs why-copy">Running a driving school means <b>juggling lesson schedules, student questions, staff changes, and constant phone calls.</b> A Voice Agent is your AI-powered assistant that answers the phone 24/7, handles routine questions, and gives your staff room to breathe—without the cost of hiring more people.</p>

<!-- Services -->
<h2 class="sec-title" style="top:1255px"><span class="accent">Services</span> for Driving Schools</h2>
<div class="service" style="left:112px"><h3>Chat Bots</h3><span class="view">View Details</span><div class="photo" role="img" aria-label="Hand holding a smartphone showing a chat bot screen" style="background:linear-gradient(135deg,#7fa6c8,#2c3f55)"></div></div>
<div class="service" style="left:359px"><h3>Voice Agent</h3><span class="view">View Details</span><div class="photo" role="img" aria-label="Woman on a phone call at a bright office desk" style="background:linear-gradient(135deg,#e9e4dc,#a89c8c)"></div></div>
<div class="service" style="left:607px"><h3>Document Processing</h3><span class="view">View Details</span><div class="photo" role="img" aria-label="Hands typing on a laptop with document icons" style="background:linear-gradient(135deg,#dfe3e8,#8a949e)"></div></div>
<div class="service" style="left:854px"><h3>Ai Based Marketing</h3><span class="view">View Details</span><div class="photo" role="img" aria-label="Team at a table reviewing AI marketing dashboards" style="background:linear-gradient(135deg,#3a4b63,#1b2535)"></div></div>

<!-- Problems -->
<div class="abs problems-bg"></div>
<div class="abs kp"><span class="tick" style="vertical-align:-1px;margin-right:4px"></span>Key Problems Solved</div>
<h2 class="sec-title" style="top:1696px">High Call Volume &amp; <span class="accent">Repetitive Questions</span></h2>
<div class="pill" style="left:166px;top:1824px"><span class="circ"></span>Pricing</div>
<div class="pill" style="left:166px;top:1903px"><span class="circ"></span>Permit Requirements</div>
<div class="pill right" style="left:771px;top:1824px">Class availability<span class="circ"></span></div>
<div class="pill right" style="left:771px;top:1903px">Road test steps<span class="circ"></span></div>
<div class="abs phone"><div class="plogo">LanePilot.ai</div><p>Let your voice<br>Agent Handle<br>Calls About:</p><div class="foot"></div></div>
<div class="abs robot" role="img" aria-label="Friendly white robot assistant waving beside the phone"></div>
<div class="abs result"><b>Result:</b> Less time answering the same questions, more time delivering great lessons.</div>
<div class="ghost" style="left:80px;top:2120px">LanePilot.ai</div>

<!-- Benefit cards -->
<div class="bcard" style="left:112px;top:2287px"><span class="ic"><svg width="44" height="44" viewBox="0 0 44 44" fill="none" stroke="#0f2350" stroke-width="2.5"><circle cx="22" cy="22" r="18"/><path d="M22 11v12h9"/></svg></span><h3>After-Hours Availability</h3><p>Missed calls = missed business. Your voice agent works evenings, weekends, and holidays.</p><p class="res"><b>Result:</b> Less time answering the same Questions, more time delivering Great lessons.</p></div>
<div class="bcard" style="left:607px;top:2287px"><span class="ic"><svg width="44" height="44" viewBox="0 0 44 44" fill="none" stroke="#0f2350" stroke-width="2.5"><circle cx="22" cy="22" r="18"/><circle cx="22" cy="17" r="6"/><path d="M11 33c3-6 19-6 22 0"/></svg></span><h3>Admin Staff Turnover</h3><p>Hiring and training office staff takes time. A voice agent is ready on day one.</p><p class="res"><b>Result:</b> Consistent, professional servic —no matter who's at the front desk.</p></div>
<div class="bcard" style="left:112px;top:2444px"><span class="ic"><svg width="44" height="44" viewBox="0 0 44 44" fill="none" stroke="#0f2350" stroke-width="2.5"><path d="M22 5 36 10v11c0 9-6 15-14 18C14 36 8 30 8 21V10z"/><path d="M16 22l5 5 8-9"/></svg></span><h3>No Expensive Tech Investment</h3><p>Voice agents run in the cloud and integrate with your existing phone system.</p><p class="res"><b>Result:</b> No hardware, low setup costs, and immediate ROI.</p></div>
<div class="bcard" style="left:607px;top:2444px"><span class="ic"><svg width="44" height="44" viewBox="0 0 44 44" fill="none" stroke="#0f2350" stroke-width="2.5"><path d="M14 8h22a4 4 0 0 1 4 4v12a4 4 0 0 1-4 4h-2v6l-6-6"/><path d="M4 18a4 4 0 0 1 4-4h16a4 4 0 0 1 4 4v10a4 4 0 0 1-4 4H13l-6 6v-6H8a4 4 0 0 1-4-4z"/><path d="M11 21v4M15 19v8M19 21v4"/></svg></span><h3>Language Barriers</h3><p>Serve more students with support for multiple languages.</p><p class="res"><b>Result:</b> Improve access and satisfaction for non-English-speaking families.</p></div>

<div class="abs side-bar" style="left:158px;top:2675px;width:182px"></div>
<div class="abs side-bar" style="left:860px;top:2675px;width:145px"></div>
<div class="abs side-bar" style="left:1008px;top:2675px;width:31px"></div>
<div class="bcard framed" style="left:340px;top:2607px"><span class="ic" style="left:34px;top:34px;width:72px;height:72px"><svg width="40" height="40" viewBox="0 0 40 40" fill="none" stroke="#0f2350" stroke-width="2.5"><rect x="5" y="8" width="30" height="27" rx="3"/><path d="M5 15h30M13 4v7M27 4v7"/><path d="M14 25a6 6 0 1 0 2-4.5M14 19v3h3"/></svg></span><h3 style="left:152px;top:22px">Instructor Absences &amp; Rescheduling</h3><p style="left:152px;top:48px;width:330px">Integrated with your booking system, your voice agent can help reschedule or notify students of changes.</p><p class="res" style="left:152px;top:92px;width:290px"><b>Result:</b> Fewer cancellations and smoother communication.</p></div>

<!-- Real benefits -->
<div class="abs rb-panel"></div>
<h2 class="abs rb-title"><b>Real Benefits</b><br>for Your School</h2>
<ul class="abs rb-list">
  <li><span class="tick"></span>24/7 live call support—no more missed calls</li>
  <li><span class="tick"></span>Faster response times = happier customers</li>
  <li><span class="tick"></span>Less admin stress for you and your team</li>
  <li><span class="tick"></span>Lower operating costs than live staff</li>
  <li><span class="tick"></span>More bookings, fewer no-shows</li>
  <li><span class="tick"></span>A modern, professional image</li>
</ul>
<div class="photo rb-photo" role="img" aria-label="Instructor with a clipboard guiding a smiling student driver inside a car"></div>

<!-- CTA -->
<section class="abs cta">
  <h2><b>Ready to Automate</b><br>Your Front Desk?</h2>
  <p>Let your school sound smarter, faster, and more helpful—24 hours a day.</p>
  <div class="btn btn-ghost" style="left:336px;width:146px">Book a Free Demo</div>
  <div class="btn btn-white" style="left:490px;width:220px">Talk to a Product Specialist</div>
  <div class="btn btn-ghost" style="left:719px;width:140px">See It in Action</div>
</section>

<!-- Testimonials -->
<h2 class="sec-title" style="top:3612px">what our <span class="accent">Clients Says</span></h2>
<div class="abs quote-card"></div>
<div class="abs quote-mark">“</div>
<div class="abs avatar" role="img" aria-label="Client portrait"></div>
<div class="abs q-name"><b>Dana Whitford</b> (Director, GreenLight Driving Academy)</div>
<p class="abs q-text">Since adding a voice agent, we've cut our call volume in half—and enrollment is up. Vivamus efficitur quam tristique velit hendrerit pellentesque et at ante. Suspendisse viverra sem in dolor semper, vel aliquam ante posuere.</p>
<div class="abs stars">★★★★★</div>
<div class="abs arrow" style="left:264px;top:3791px"></div>
<div class="abs arrow" style="left:915px;top:3791px"></div>
<div class="ghost" style="left:80px;top:3935px">LanePilot.ai</div>

<!-- Footer -->
<footer class="abs footer"></footer>
<div class="abs brand" style="left:112px;top:4140px;color:#fff"><span class="dot"></span>LanePilot.ai</div>
<p class="abs f-desc">Running a driving school means juggling lesson schedules, student questions, staff changes, and constant phone calls.</p>
<div class="abs f-div" style="left:368px"></div>
<div class="abs f-div" style="left:605px"></div>
<div class="abs f-div" style="left:831px"></div>
<div class="abs f-head" style="left:439px;top:4108px;color:#fff">Main Links</div>
<ul class="abs f-links" style="left:439px;top:4138px"><li>Home</li><li>Services</li><li>Why Driving Schools</li><li>About</li><li>Pricing</li><li>FAQS</li><li>Demos</li><li>Contact Us</li></ul>
<div class="abs f-head" style="left:664px;top:4108px;color:#fff">Follow Us On</div>
<div class="abs" style="left:664px;top:4138px">
  <div class="f-social"><i></i>Friendlane</div>
  <div class="f-social"><i></i>Snapshot Hub</div>
  <div class="f-social"><i></i>ClipStream</div>
</div>
<div class="abs f-head" style="left:864px;top:4108px;color:#fff">Subscribe Newsletter</div>
<div class="abs f-input">Enter Your Email</div>
<div class="btn btn-green" style="left:864px;top:4199px;width:160px;height:44px;font-weight:500">Subscribe</div>
<div class="abs f-copy">Copyright © LanePilot.ai 2025 All Rights Reserved</div>

</body>
</html>
```